Torvane Center for Restorative Medicine

I need a full informational website for my medical practice. I would like to use my logo and also include a lot of emblems/pictures (also a picture of me in a white coat). The website should have a function for people to inquire and send me messages. I will be offering needle-less regenerative injection therapy, stem cell treatments, bioidentical hormone therapy, treatment for chronic illness, neurodegenerative diseases, skin rejuvenation, hair restoration, male enhancement, female enhancement, and anti-aging. The practice will not be accepting insurance and will be cash/credit card only.
A good example of written content and functionality is this website:
http://thebqvx.example/. However, I want different theme and tones.
Target Market(s)
High end clientele in Los Angeles, Southern California. Health minded people who are interested in living better and longer and can afford anti-aging treatments. Men and women who want to improve sexual health and wellbeing.
Industry/Entity Type
Medical And Science
Coding
Coded - Design and coding required
Number of Pages Required
5+ page
Font styles to use
Requirements
Must have
- 1. I will need to be able to move the site to other servers (needed for site speed)
- 2. Site must be build on WordPress
- 3. Full admin credentials for domain, cpanel, wordpress, ftp.
- 4. No third party interaction on development and content deployment once the site is on different servers
- 5. I will need the ability to add content and links to the site
- 6. I will need the ability to optimize the site for speed
- 7. I will need to ability to modify URLs so they are more SEO friendly
Nice to have
- pictures of stem cells, health improvement and regeneration, beauty, youthful individuals, older healthy and happy individuals. Medical designs.
Should not have
- flowers, dna

```html
<!DOCTYPE html>
<html lang="en">
<head>
<meta charset="utf-8">
<title>Torvane Center for Restorative Medicine</title>
<link rel="stylesheet" href="https://fonts.googleapis.com/css2?family=Cinzel:wght@600;700&family=Lato:wght@300;400;700&family=Open+Sans:wght@300;400;600;700&display=swap">
<style>
:root{
  --green:#1aa985;
  --green-dark:#13906f;
  --navy:#122b82;
  --ink:#222;
  --muted:#666;
  --pale:#edf6f8;
  --field:#ececec;
  --hero:#f3f3f3;
  --white:#fff;
  --star:#f5b81c;
}
*{margin:0;padding:0;box-sizing:border-box}
html,body{width:1200px;height:3711px;overflow:hidden}
body{position:relative;font-family:'Lato',sans-serif;color:var(--ink);background:var(--white)}
.abs{position:absolute}
section,header,footer{position:absolute;left:0;width:1200px}
.heading{font-family:'Cinzel',serif;font-weight:700;color:var(--navy);text-align:center;width:100%}
.btn{position:absolute;background:var(--green);color:#fff;border-radius:30px;font-family:'Cinzel',serif;font-weight:600;display:flex;align-items:center;justify-content:center;letter-spacing:1px}

/* header */
.site-header{top:0;height:94px;background:var(--white);z-index:3;box-shadow:0 1px 3px rgba(0,0,0,.05)}
.nav-item{position:absolute;top:27px;height:42px;display:flex;align-items:center;font-size:16px;color:#333;letter-spacing:.3px}
.nav-item.active{background:var(--green);color:#fff;border-radius:22px;padding:0 20px}
.brand-disc{position:absolute;left:500px;top:-10px;width:200px;height:196px;border-radius:50%;background:var(--white);z-index:4;display:flex;flex-direction:column;align-items:center;justify-content:center}
.brand-dot{width:48px;height:48px;border-radius:50%;background:var(--navy);margin-bottom:8px;margin-top:30px}
.brand-name{font-family:'Lato',sans-serif;font-weight:700;font-size:34px;color:var(--navy);letter-spacing:1px}
.phone{position:absolute;left:953px;top:34px;display:flex;align-items:center;gap:10px;font-weight:700;font-size:19px;color:#222}

/* hero */
.hero{top:94px;height:582px;background:var(--hero)}
.hero-figure{position:absolute;left:495px;top:0;width:705px;height:582px;background:radial-gradient(ellipse 38% 46% at 50% 52%,rgba(60,110,210,.55),rgba(80,170,120,.3) 55%,rgba(243,243,243,0) 100%)}
.hero-title{left:77px;top:146px;width:620px;font-family:'Open Sans',sans-serif;font-weight:400;font-size:38px;line-height:50px;color:#1d1d1d;letter-spacing:-.5px}
.hero-sub{left:77px;top:258px;font-family:'Open Sans',sans-serif;font-weight:700;font-size:20px;line-height:28px;color:#111}
.hero-text{left:77px;top:294px;width:420px;font-family:'Open Sans',sans-serif;font-size:14px;line-height:24px;color:#666}

/* welcome */
.welcome{top:676px;height:351px}
.welcome .heading{position:absolute;top:58px;font-size:45px}
.welcome-tag{position:absolute;top:120px;width:100%;text-align:center;font-size:16px;color:var(--green)}
.welcome-text{position:absolute;left:198px;top:152px;width:804px;text-align:center;font-size:14px;line-height:24px;color:var(--muted)}
.chevron{position:absolute;left:578px;top:247px;width:44px;height:44px;border-radius:50%;background:var(--green)}

/* services */
.services{top:1027px;height:680px;background:var(--pale)}
.services .heading{position:absolute;top:62px;font-size:45px}
.service-card{position:absolute;top:141px;width:248px;height:383px;background:var(--white);text-align:center}
.service-photo{position:absolute;left:37px;top:29px;width:174px;height:174px;border-radius:50%;border:4px solid #7fcfc2}
.service-title{position:absolute;top:229px;width:100%;font-family:'Cinzel',serif;font-weight:700;font-size:17px;line-height:23px;color:var(--navy)}
.service-text{position:absolute;left:20px;top:287px;width:208px;font-size:14px;line-height:22px;color:var(--muted)}

/* doctor */
.doctor{top:1707px;height:594px}
.doctor-photo{left:173px;top:62px;width:359px;height:532px;background:linear-gradient(180deg,#e9d1b9 0%,#f1ece8 40%,#e4e8ec 100%);border-radius:180px 180px 0 0}
.doctor-title{left:609px;top:86px;font-family:'Cinzel',serif;font-weight:700;font-size:45px;color:var(--navy)}
.doctor-text{left:609px;width:480px;font-size:14px;line-height:28px;color:var(--muted)}

/* testimonials */
.testimonials{top:2301px;height:564px;background:radial-gradient(circle at 15% 40%,rgba(255,255,255,.08) 0 120px,transparent 121px),radial-gradient(circle at 85% 70%,rgba(255,255,255,.07) 0 150px,transparent 151px),linear-gradient(180deg,#149c7c,#1bb08a);color:#fff}
.testimonials .heading{position:absolute;top:60px;font-size:45px}
.testi-sub{position:absolute;top:120px;width:100%;text-align:center;font-size:16px;color:#fff}
.testi{position:absolute;top:163px;width:300px;text-align:center}
.avatar{width:129px;height:129px;border-radius:50%;border:4px solid #fff;margin:0 auto;background:linear-gradient(160deg,#7a5a45,#c9a68c)}
.testi-name{margin-top:20px;font-family:'Open Sans',sans-serif;font-weight:600;font-size:23px}
.testi-rule{width:64px;height:2px;background:#fff;margin:10px auto 12px}
.testi-text{font-size:14px;line-height:24px;color:#eafaf5}
.stars{margin-top:14px;display:flex;justify-content:center;gap:3px}
.client{margin-top:4px;font-size:15px}

/* contact */
.contact{top:2865px;height:512px}
.contact .heading{position:absolute;top:60px;font-size:45px}
.contact-text{position:absolute;left:228px;top:118px;width:744px;text-align:center;font-size:14px;line-height:25px;color:var(--muted)}
.field{position:absolute;background:var(--field);font-size:13px;color:#777;padding:12px 14px}

/* footer */
.site-footer{top:3377px;height:267px;background:var(--pale)}
.foot-brand{left:119px;top:54px;width:166px;text-align:center}
.foot-dot{width:44px;height:44px;border-radius:50%;background:var(--navy);margin:0 auto 8px}
.foot-name{font-weight:700;font-size:32px;color:var(--navy)}
.social{position:absolute;top:178px;width:44px;height:44px;border-radius:50%;background:var(--green)}
.foot-title{font-family:'Cinzel',serif;font-weight:700;font-size:20px;color:var(--navy);top:44px}
.sitemap{left:344px;top:86px;list-style:none;font-size:14px;color:#444}
.sitemap li{height:26.5px;padding-left:18px;position:relative}
.sitemap li::before{content:"";position:absolute;left:2px;top:6px;width:7px;height:7px;border-radius:50%;background:var(--green)}
.contact-row{left:605px;display:flex;gap:14px;font-size:14px;color:#444;line-height:20px}
.emerg-num{left:876px;top:88px;font-weight:700;font-size:29px;color:var(--green)}
.emerg-text{left:876px;top:136px;width:230px;font-size:14px;line-height:22px;color:#444}
.copyright{top:3644px;height:67px;background:#dfeef3;display:flex;align-items:center;justify-content:center;font-size:13px;color:#444}
</style>
</head>
<body>

<header class="site-header">
  <div class="nav-item active" style="left:129px">HOME</div>
  <div class="nav-item" style="left:238px">ABOUT</div>
  <div class="nav-item" style="left:324px">SERVICES</div>
  <div class="nav-item" style="left:428px">DR.BIO</div>
  <div class="brand-disc"><div class="brand-dot"></div><div class="brand-name">TORVANE</div></div>
  <div class="nav-item" style="left:715px">TESTIMONILAS</div>
  <div class="nav-item" style="left:856px">CONTACT</div>
  <div class="phone">
    <svg width="26" height="26" viewBox="0 0 26 26"><circle cx="13" cy="13" r="11.5" fill="none" stroke="#1aa985" stroke-width="2"/><path d="M9 7.5c.8-.5 1.5-.3 1.9.4l1 2c.3.6.1 1.2-.4 1.5l-.7.4c.6 1.5 1.7 2.6 3.2 3.2l.4-.7c.3-.5.9-.7 1.5-.4l2 1c.7.4.9 1.1.4 1.9-1 1.4-2.6 1.7-4.3.8-2.4-1.2-4.2-3-5.4-5.4-.9-1.7-.6-3.3.4-4.7z" fill="#1aa985"/></svg>
    123 456 7890
  </div>
</header>

<section class="hero">
  <div class="hero-figure" role="img" aria-label="Human figure formed from blue and green particles with arms outstretched"></div>
  <h1 class="abs hero-title">Regenerative medicine is the<br>medicine of the future.</h1>
  <p class="abs hero-sub">It is time that we go back to the origin.</p>
  <p class="abs hero-text">Lorem Ipsum is simply dummy text of the printing and type setting industry. Lorem Ipsum has been the industry's standard dummy text ever since the.</p>
  <div class="btn" style="left:77px;top:379px;width:198px;height:49px;font-size:19px">CONTACT US</div>
</section>

<section class="welcome">
  <h2 class="heading">Welcome To Torvane</h2>
  <p class="welcome-tag">Center for Restorative Medicine</p>
  <p class="welcome-text">Lorem Ipsum is simply dummy text of the printing and typesetting industry. Lorem Ipsum has been the industry's standard dummy text ever since the 1500s, when an unknown printer took a galley of type and scrambled it to make a type specimen book. It has survived not only five centuries, but also the leap</p>
  <div class="chevron"><svg width="44" height="44" viewBox="0 0 44 44"><path d="M16 16l6 6 6-6M16 22l6 6 6-6" fill="none" stroke="#fff" stroke-width="2.4" stroke-linecap="round" stroke-linejoin="round"/></svg></div>
</section>

<section class="services">
  <h2 class="heading">Service We Provided</h2>
  <article class="service-card" style="left:79px">
    <div class="service-photo" role="img" aria-label="Woman touching her smooth skin" style="background:linear-gradient(160deg,#f4e3d5,#d8b79c)"></div>
    <h3 class="service-title">Skin<br>Rejuvenation</h3>
    <p class="service-text">Lorem Ipsum is simply dummy text of the printing and type setting industry.</p>
  </article>
  <article class="service-card" style="left:344px">
    <div class="service-photo" role="img" aria-label="Person's back with highlighted area of pain" style="background:linear-gradient(160deg,#f3ece8,#e39a8a)"></div>
    <h3 class="service-title">Stem Cell<br>Treatments</h3>
    <p class="service-text">Lorem Ipsum is simply dummy text of the printing and type setting industry.</p>
  </article>
  <article class="service-card" style="left:609px">
    <div class="service-photo" role="img" aria-label="Woman resting her head on her hand" style="background:linear-gradient(160deg,#c67a4e,#f0dccb)"></div>
    <h3 class="service-title">Bioidentical<br>Hormone Therapy</h3>
    <p class="service-text">Lorem Ipsum is simply dummy text of the printing and type setting industry.</p>
  </article>
  <article class="service-card" style="left:874px">
    <div class="service-photo" role="img" aria-label="Colourful pills and a syringe" style="background:linear-gradient(160deg,#f7c6d4,#9fd6e8)"></div>
    <h3 class="service-title">Treatment for<br>Chronic Illness</h3>
    <p class="service-text">Lorem Ipsum is simply dummy text of the printing and type setting industry.</p>
  </article>
  <div class="btn" style="left:512px;top:559px;width:176px;height:49px;font-size:19px">VIEW ALL</div>
</section>

<section class="doctor">
  <div class="abs doctor-photo" role="img" aria-label="Doctor in a white coat with a stethoscope, arms crossed"></div>
  <h2 class="doctor-title abs">Dr. Bio</h2>
  <p class="abs doctor-text" style="top:150px">Lorem Ipsum is simply dummy text of the printing and typesetting industry. Lorem Ipsum has been the industry's standard dummy text ever since the 1500s, when an unknown printer took a galley of</p>
  <p class="abs doctor-text" style="top:244px">Lorem Ipsum is simply dummy text of the printing and typesetting industry. Lorem Ipsum has been the industry's standard dummy text ever since the 1500s, when an unknown printer took a galley of type and scrambled it to make a type specimen book.</p>
  <p class="abs doctor-text" style="top:366px">Lorem Ipsum is simply dummy text of the printing and typesetting industry. Lorem Ipsum has been the industry's stand</p>
  <div class="btn" style="left:609px;top:445px;width:341px;height:52px;font-size:21px">BOOK AN APPOINTMENT</div>
</section>

<section class="testimonials">
  <h2 class="heading" style="color:var(--navy)">Patient Testimonials</h2>
  <p class="testi-sub">It's always the word of mouth that's the best advice. Here are some of our...</p>
  <svg class="abs" style="left:28px;top:285px" width="20" height="40" viewBox="0 0 20 40"><path d="M16 4L4 20l12 16" fill="none" stroke="rgba(255,255,255,.6)" stroke-width="2"/></svg>
  <svg class="abs" style="left:1152px;top:285px" width="20" height="40" viewBox="0 0 20 40"><path d="M4 4l12 16L4 36" fill="none" stroke="rgba(255,255,255,.6)" stroke-width="2"/></svg>
  <div class="testi" style="left:92px">
    <div class="avatar" role="img" aria-label="Portrait of a smiling patient"></div>
    <div class="testi-name">Helped Me a Lot</div><div class="testi-rule"></div>
    <p class="testi-text">Lorem Ipsum is simply dummy text of the printing and typesetting industry. Lorem Ipsum has been the industry's stand</p>
    <div class="stars"><svg width="110" height="20" viewBox="0 0 110 20"><g fill="#f5b81c"><path id="st" d="M10 1l2.6 6 6.4.5-4.9 4.2 1.5 6.3L10 14.6 4.4 18l1.5-6.3L1 7.5 7.4 7z"/><use href="#st" x="22"/><use href="#st" x="44"/><use href="#st" x="66"/><use href="#st" x="88"/></g></svg></div>
    <div class="client">client name</div>
  </div>
  <div class="testi" style="left:450px">
    <div class="avatar" role="img" aria-label="Portrait of a smiling patient" style="background:linear-gradient(160deg,#5a3a2a,#e0b79a)"></div>
    <div class="testi-name">Awesome Optometrist</div><div class="testi-rule"></div>
    <p class="testi-text">Lorem Ipsum is simply dummy text of the printing and typesetting industry. Lorem Ipsum has been the industry's stand</p>
    <div class="stars"><svg width="110" height="20" viewBox="0 0 110 20"><g fill="#f5b81c"><use href="#st"/><use href="#st" x="22"/><use href="#st" x="44"/><use href="#st" x="66"/><use href="#st" x="88"/></g></svg></div>
    <div class="client">client name</div>
  </div>
  <div class="testi" style="left:805px">
    <div class="avatar" role="img" aria-label="Portrait of a smiling patient" style="background:linear-gradient(160deg,#6b5644,#e6c3a8)"></div>
    <div class="testi-name">My vision is Perfect</div><div class="testi-rule"></div>
    <p class="testi-text">Lorem Ipsum is simply dummy text of the printing and typesetting industry. Lorem Ipsum has been the industry's stand</p>
    <div class="stars"><svg width="110" height="20" viewBox="0 0 110 20"><g fill="#f5b81c"><use href="#st"/><use href="#st" x="22"/><use href="#st" x="44"/><use href="#st" x="66"/><use href="#st" x="88"/></g></svg></div>
    <div class="client">client name</div>
  </div>
</section>

<section class="contact">
  <h2 class="heading">Contact Us</h2>
  <p class="contact-text">Lorem Ipsum is simply dummy text of the printing and typesetting industry&nbsp; has been the industry's stand Lorem Ipsum is simply dummy text of the printing and typesetting industry</p>
  <div class="field" style="left:215px;top:210px;width:312px;height:47px">Name *</div>
  <div class="field" style="left:215px;top:267px;width:312px;height:47px">Email *</div>
  <div class="field" style="left:215px;top:324px;width:312px;height:47px">Phone *</div>
  <div class="field" style="left:539px;top:210px;width:446px;height:161px">Message *</div>
  <div class="btn" style="left:527px;top:396px;width:144px;height:49px;font-size:19px">SUBMIT</div>
</section>

<footer class="site-footer">
  <div class="abs foot-brand"><div class="foot-dot"></div><div class="foot-name">TORVANE</div></div>
  <div class="social" style="left:129px"></div>
  <div class="social" style="left:181px"></div>
  <div class="social" style="left:233px"></div>

  <h4 class="abs foot-title" style="left:344px">Sitemap</h4>
  <ul class="abs sitemap">
    <li>Home</li><li>About</li><li>Services</li><li>Dr.Bio</li><li>Testimonial</li><li>Contact</li>
  </ul>

  <h4 class="abs foot-title" style="left:611px">Contect Us</h4>
  <div class="abs contact-row" style="top:86px">
    <svg width="22" height="30" viewBox="0 0 22 30"><path d="M11 1C5.5 1 1 5.4 1 10.8 1 18 11 29 11 29s10-11 10-18.2C21 5.4 16.5 1 11 1z" fill="#1aa985"/><circle cx="11" cy="10.5" r="3.8" fill="#edf6f8"/></svg>
    <div><strong style="color:var(--navy)">Torvane</strong><br>101 - Lorem ipsum is simple<br>text of print type texty</div>
  </div>
  <div class="abs contact-row" style="top:164px">
    <svg width="22" height="22" viewBox="0 0 22 22"><path d="M5 2c1-.6 1.9-.3 2.4.5l1.3 2.6c.4.8.1 1.5-.5 1.9l-.9.5c.8 2 2.2 3.4 4.2 4.2l.5-.9c.4-.6 1.1-.9 1.9-.5l2.6 1.3c.8.5 1.1 1.4.5 2.4-1.3 1.8-3.3 2.2-5.5 1-3.1-1.6-5.4-3.9-7-7C2.8 5.3 3.2 3.3 5 2z" fill="#1aa985"/></svg>
    <div>123 456 7890</div>
  </div>
  <div class="abs contact-row" style="top:210px">
    <svg width="22" height="18" viewBox="0 0 22 18"><rect x="1" y="1" width="20" height="16" rx="2" fill="#1aa985"/><path d="M2 3l9 7 9-7" fill="none" stroke="#edf6f8" stroke-width="1.6"/></svg>
    <div>info@torvane.example</div>
  </div>

  <h4 class="abs foot-title" style="left:876px">Emergency Number</h4>
  <div class="abs emerg-num">123 456 7890</div>
  <p class="abs emerg-text">Call us now if you are in a medical emergency need, we will reply swiftly and provide you with a medical aid.</p>
</footer>

<div class="abs copyright" style="left:0;width:1200px">©TORVANE Center for Restorative Medicine - 2018 All Right Reserved. Terms of Use</div>

</body>
</html>
```